Torvaline business cards

Need fresh design for our business cards. Logo must be specific, we are open for everything else.

Contact Information for Business Card

phrase "GMP & JANITORIAL SERVICES" should be used as main point of card

Colors
3176b5
3276b5
85acd3
cedeed
ffffff
0292cd
33a6d7
85cae6
cee9f5

Requirements
Must have
• The logo
Should not have
• crowded designs

```html
<!DOCTYPE html>
<html lang="en">
<head>
<meta charset="utf-8">
<title>Torvaline business cards</title>
<link rel="stylesheet" href="https://fonts.googleapis.com/css2?family=Jost:wght@400;500&display=swap">
<style>
  :root {
    --blue-deep: #3176b5;
    --blue-mid: #85acd3;
    --blue-pale: #cedeed;
    --cyan: #0292cd;
    --cyan-soft: #85cae6;
    --cyan-pale: #cee9f5;
    --white: #ffffff;
    --stage: #eef1ea;
    --logo-blue: #1f7fc1;
  }
  * { box-sizing: border-box; margin: 0; padding: 0; }
  html, body {
    width: 1200px; height: 835px; overflow: hidden;
    background: var(--stage);
    font-family: "Jost", "Futura", sans-serif;
  }
  .canvas {
    position: relative; width: 1200px; height: 835px;
  }
  .card {
    position: absolute; top: 268px;
    width: 520px; height: 300px;
    background: var(--white);
    box-shadow: 0 10px 30px rgba(60, 80, 40, 0.18);
    overflow: hidden;
  }
  .card--back { left: 50px; }
  .card--front { left: 630px; }

  /* back side */
  .card__headline {
    position: absolute; left: 34px; top: 30px;
    font-size: 29px; font-weight: 400; letter-spacing: 0.5px;
    color: var(--blue-mid); white-space: nowrap;
  }
  .card__logo-small {
    position: absolute; left: 34px; top: 96px;
    font-size: 24px; font-weight: 500; letter-spacing: 3px;
    color: var(--logo-blue);
  }
  .card__name {
    position: absolute; left: 34px; top: 140px; width: 220px;
    text-align: right;
    font-size: 30px; font-weight: 400; line-height: 1.05;
    color: var(--blue-deep); text-transform: uppercase;
  }
  .contact {
    position: absolute; left: 280px; top: 168px;
    list-style: none;
    font-size: 13px; color: var(--blue-deep);
  }
  .contact__item {
    display: flex; align-items: center; gap: 8px;
    line-height: 1; margin-bottom: 9px; white-space: nowrap;
  }
  .contact__icon { width: 12px; height: 12px; flex: none; }

  /* front side */
  .card__texture {
    position: absolute; inset: 0;
    background:
      radial-gradient(circle at 20% 30%, rgba(206,222,237,0.45), transparent 40%),
      radial-gradient(circle at 80% 75%, rgba(206,233,245,0.5), transparent 45%),
      var(--white);
  }
  .card__logo-large {
    position: absolute; left: 0; right: 0; top: 112px;
    text-align: center;
    font-size: 62px; font-weight: 500; letter-spacing: 8px;
    color: var(--logo-blue);
  }
</style>
</head>
<body>
<main class="canvas">

  <section class="card card--back" aria-label="Card back">
    <h1 class="card__headline">GMP &amp; JANITORIAL SERVICES</h1>
    <p class="card__logo-small">TORVALINE</p>
    <p class="card__name">Name<br>Last Name</p>
    <ul class="contact">
      <li class="contact__item">
        <svg class="contact__icon" viewBox="0 0 12 12"><path d="M6 0.5a3.8 3.8 0 0 0-3.8 3.8C2.2 7 6 11.5 6 11.5s3.8-4.5 3.8-7.2A3.8 3.8 0 0 0 6 0.5z" fill="#3176b5"/><circle cx="6" cy="4.3" r="1.4" fill="#fff"/></svg>
        No#, Main Road, Main Road 2, City
      </li>
      <li class="contact__item">
        <svg class="contact__icon" viewBox="0 0 12 12"><circle cx="6" cy="6" r="5" fill="none" stroke="#3176b5" stroke-width="1.2"/><ellipse cx="6" cy="6" rx="2.2" ry="5" fill="none" stroke="#3176b5" stroke-width="1"/><path d="M1 6h10" stroke="#3176b5" stroke-width="1"/></svg>
        0888 888 888
      </li>
      <li class="contact__item">
        <svg class="contact__icon" viewBox="0 0 12 12"><rect x="3" y="0.8" width="6" height="10.4" rx="1" fill="none" stroke="#3176b5" stroke-width="1.1"/><circle cx="6" cy="9.4" r="0.6" fill="#3176b5"/></svg>
        torvaline
      </li>
      <li class="contact__item">
        <svg class="contact__icon" viewBox="0 0 12 12"><rect x="0.5" y="2.5" width="11" height="7.5" fill="#3176b5"/><path d="M0.8 2.8L6 6.8l5.2-4" fill="none" stroke="#fff" stroke-width="1"/></svg>
        torvaline@email.com
      </li>
      <li class="contact__item">
        <span class="contact__icon"></span>
        torvaline.com
      </li>
    </ul>
  </section>

  <section class="card card--front" aria-label="Card front">
    <div class="card__texture" role="img" aria-label="Scattered water droplets over a white surface"></div>
    <p class="card__logo-large">TORVALINE</p>
  </section>

</main>
</body>
</html>
```